Corporate Wall Mural for Office

We have several offices across North America and we want to have a corporate wall mural in each office, so we require a mural wall design that can be adjusted for different wall dimensions and still look good.

The first mural will be 239.5" x 112.5" it will be in our Toronto office - so the background city will be the Toronto skyline

I have attached a draft design and the content PNG file.

We want a different design that keeps the content outlined in the Mural Design Content PNG file.

Our corporate font is Gilroy Semi Bold

Our corporate colors are
Blue
C94
M70
Y0
K12
Pantone 2945C

Purple
C 80
M 78
PMS 2368 C

Sky Blue
C68
M34
PMS 2727 C
Our website is qorbelta.com

Founded in 2012, QBL is a leading provider of technology infrastructure solutions, specializing in Broadband, DAS/Private Networks, Fixed Wireless Access, Site Solutions, Carrier Networks, and Test & Measurement. Our mission is to empower organizations of all sizes with innovative connectivity and telecom infrastructure solutions to build the future of communications.

Target Market(s)

Target is the staff and visitors of our office

Industry/Entity Type

network infrastructure: both wireless and wireline

Font styles to use
Sans Serif
Other font styles liked:
• Gilroy Semi-Bold and Bold

Colors
0054AA
0677BA
7BADD7
CADEEF
E8F1F8

Requirements
Must have
• the info listed in the Mural Content.png file, our corporate colors. It should be bright and energetic.
Nice to have
• I like concept of the city silhouette from the draft design

```html
<!DOCTYPE html>
<html lang="en">
<head>
<meta charset="UTF-8">
<title>QBL Office Mural</title>
<link rel="stylesheet" href="https://fonts.googleapis.com/css2?family=Roboto:ital,wght@0,300;0,400;0,500;0,700;0,900;1,700;1,900&display=swap">
<style>
  :root {
    --navy: #0e1d44;
    --deep-blue: #1c3f8a;
    --brand-blue: #1d4f9c;
    --sky: #5b92d4;
    --band-blue: #4d86c6;
    --purple: #5a3f96;
    --purple-text: #5b46a3;
    --panel: #dadee7;
    --ice: #e6eaf1;
    --teal: #1aa3a6;
    --cyan: #3fd6e6;
    --ink: #111;
    --white: #fff;
  }
  * { box-sizing: border-box; margin: 0; padding: 0; }
  html, body { width: 1200px; height: 564px; overflow: hidden; background: var(--white); }
  body { font-family: "Roboto", Arial, sans-serif; }
  .mural { position: relative; width: 1200px; height: 564px; overflow: hidden; background: var(--navy); }

  .skyline {
    position: absolute; inset: 0;
    background:
      radial-gradient(ellipse 420px 180px at 640px 470px, rgba(63,214,230,.55), transparent 70%),
      radial-gradient(ellipse 300px 140px at 900px 450px, rgba(63,214,230,.4), transparent 70%),
      linear-gradient(180deg, #0c1b40 0%, #10285a 55%, #1a6f92 82%, #2bb8c9 100%);
  }
  .teal-orb { position: absolute; left: 1114px; top: 228px; width: 344px; height: 344px; border-radius: 50%; background: var(--teal); }

  .left-shape { position: absolute; inset: 0; width: 1200px; height: 564px; }

  .header-band { position: absolute; left: 300px; top: 36px; width: 900px; height: 62px; background: var(--band-blue); }
  .headline {
    position: absolute; left: 440px; top: 48px; width: 720px; text-align: center;
    font-weight: 900; font-style: italic; font-size: 33px; color: var(--navy); letter-spacing: -.2px;
  }
  .subline {
    position: absolute; left: 491px; top: 98px; width: 587px; height: 26px;
    background: var(--white); border-radius: 0 0 18px 18px;
    text-align: center; font-size: 15px; font-weight: 400; line-height: 26px; color: var(--ink);
  }

  .brand { position: absolute; left: 56px; top: 38px; display: flex; align-items: center; gap: 14px; }
  .brand-dot { width: 56px; height: 56px; border-radius: 50%; background: var(--brand-blue); }
  .brand-name { font-size: 50px; font-weight: 700; color: var(--ink); letter-spacing: -1px; }

  .unique-title {
    position: absolute; left: 50px; top: 147px;
    font-size: 22.5px; font-weight: 900; font-style: italic; color: var(--purple-text);
  }
  .unique-item { position: absolute; left: 50px; font-size: 15.8px; font-weight: 300; line-height: 18.5px; color: var(--ink); }
  .unique-item strong { font-weight: 700; }
  .unique-item .tagline { display: block; font-size: 11.8px; font-weight: 700; }
  .item-touch { top: 190px; }
  .item-experience { top: 242px; }
  .item-solution { top: 309px; }

  .info-card {
    position: absolute; border: 2px solid rgba(255,255,255,.85); border-radius: 38px;
    background: rgba(40,72,165,.72); color: var(--white); padding-left: 24px;
  }
  .info-card.purple { background: rgba(96,74,168,.78); }
  .info-card h2 { font-size: 14px; font-weight: 700; letter-spacing: .2px; margin-bottom: 14px; }
  .info-card ul { list-style: none; font-size: 13px; font-weight: 300; line-height: 15.3px; }
  .info-card li::before { content: "• "; font-size: 9px; vertical-align: 2px; }
  .card-capabilities { left: 335px; top: 205px; width: 187px; height: 242px; padding-top: 53px; }
  .card-services { left: 645px; top: 196px; width: 187px; height: 172px; padding-top: 53px; }
  .card-markets { left: 915px; top: 205px; width: 187px; height: 242px; padding-top: 53px; padding-left: 18px; }
  .card-markets .indent { padding-left: 9px; }
  .card-markets .cont::before { content: none; }

  .values-band {
    position: absolute; left: 17px; top: 461px; width: 1015px; height: 91px;
    background: rgba(230,234,241,.93); border-radius: 0 46px 46px 0;
  }
  .values-label {
    position: absolute; left: 17px; top: 492px; width: 248px; height: 28px;
    background: var(--sky); border-radius: 0 20px 0 0;
    padding-left: 39px; font-size: 24px; font-weight: 900; font-style: italic; line-height: 28px; color: var(--purple-text);
    white-space: nowrap;
  }
  .value-pill {
    position: absolute; top: 488px; width: 126px; height: 36px; border-radius: 18px;
    display: flex; align-items: center; justify-content: center; text-align: center;
    font-size: 15.5px; font-weight: 500; line-height: 14.5px;
  }
  .value-pill.sky { background: var(--sky); color: var(--navy); }
  .value-pill.violet { background: var(--purple); color: var(--white); }
</style>
</head>
<body>
<main class="mural">
  <div class="skyline" role="img" aria-label="Glowing line-art city skyline with a tall broadcast tower and a network of connected light points over a dark night sky"></div>
  <div class="teal-orb"></div>

  <svg class="left-shape" viewBox="0 0 1200 564" aria-hidden="true">
    <path d="M17 0 H410 C330 60 300 200 300 300 C295 400 250 470 150 564 H17 Z" fill="var(--panel)"/>
    <path d="M410 0 C330 60 300 200 300 300 C295 400 250 470 150 564" fill="none" stroke="var(--sky)" stroke-width="6"/>
    <path d="M425 0 C345 60 318 200 316 300 C312 400 270 480 180 564" fill="none" stroke="var(--brand-blue)" stroke-width="6"/>
    <path d="M445 0 C360 60 334 200 332 300 C328 410 290 490 210 564" fill="none" stroke="var(--purple)" stroke-width="6"/>
    <rect x="0" y="0" width="17" height="564" fill="var(--purple)"/>
  </svg>

  <div class="header-band"></div>
  <h1 class="headline">Enabling Solutions for a Connected World</h1>
  <p class="subline">We Distribute Products and Solution Services for Digital Infrastructure</p>

  <div class="brand">
    <span class="brand-dot"></span>
    <span class="brand-name">QBL</span>
  </div>

  <h2 class="unique-title">What Makes Us Unique?</h2>
  <p class="unique-item item-touch"><strong>QBL Touch:</strong> We are more<br>than a catalog.</p>
  <p class="unique-item item-experience"><strong>QBL Experience:</strong> A pleasure<br>to do business with.<span class="tagline">Proactive, Professional and Precise.</span></p>
  <p class="unique-item item-solution"><strong>QBL Solution:</strong> Design,<br>Develop, and Deliver<br>Custom Solutions; On-Time<br>and On-Spec</p>

  <section class="info-card card-capabilities">
    <h2>Our Capabilities</h2>
    <ul>
      <li>Wireless Infrastructure</li>
      <li>Broadband &amp; Fiber</li>
      <li>Site Solutions</li>
      <li>Fixed Wireless Access</li>
      <li>Test &amp; Measurement</li>
      <li>DAS &amp; PWN</li>
      <li>Power Solutions</li>
    </ul>
  </section>

  <section class="info-card purple card-services">
    <h2>Solutions Services</h2>
    <ul>
      <li>Kitting &amp; Logistics</li>
      <li>Professional Engineering</li>
      <li>Placeholder</li>
    </ul>
  </section>

  <section class="info-card card-markets">
    <h2>Our Markets</h2>
    <ul>
      <li>Carriers &amp; Cable</li>
      <li class="cont indent">Companies</li>
      <li>Data Centers</li>
      <li>Utilities</li>
      <li>Federal Government</li>
      <li>Education</li>
      <li>Industrial Manufacturing</li>
      <li class="cont">&amp; Digital Supply Chain</li>
    </ul>
  </section>

  <div class="values-band"></div>
  <div class="values-label">Our Core Values</div>
  <div class="value-pill sky" style="left:290px">People First</div>
  <div class="value-pill violet" style="left:433px">Intellectual<br>Curiosity</div>
  <div class="value-pill sky" style="left:578px">Continuous<br>Improvement</div>
  <div class="value-pill violet" style="left:720px">Customer<br>Focus</div>
  <div class="value-pill sky" style="left:867px">Results<br>Matter</div>
</main>
</body>
</html>
```